Maritime Law Firm Business Card Design Project

We are a new maritime law firm starting in Queensland, Australia. The principal is a master mariner as well as a lawyer and is looking for a logo design that evokes a practical and user-friendly approach to the law, as well as maritime law expertise.

We would like to use the compass rose as the foundation for the design, as it symbolises clarity of direction and purpose, as well as traditional maritime heritage.

The 16th Century Luis Bercedo Compass Rose (attached) is beautiful, but is too complex for a logo. A simplified version is desired.

Colour Paletter s flexible, although a B&W version is also needed. Colour suggestions are navy blue (for the sea), red and green (navigation lights) and maroon (for Queensland).

Target Market(s)

Maritime Industry/legal services

Industry/Entity Type

Law Firm

Font styles to use
Sans Serif

Requirements
Must have
• Contact Details
Name of 'Pellworth Legal'

```html
<!DOCTYPE html>
<html lang="en">
<head>
<meta charset="utf-8">
<title>Pellworth Legal – Business Card</title>
<link rel="stylesheet" href="https://fonts.googleapis.com/css2?family=Open+Sans:wght@400;600;700&display=swap">
<style>
  :root {
    --bg: #e9e9ec;
    --navy: #0d1a3a;
    --navy-deep: #07102a;
    --blue: #3b7fd1;
    --ink: #1a2340;
    --muted: #4a4f5c;
    --white: #ffffff;
    --faint: #eceef2;
  }
  * { margin: 0; padding: 0; box-sizing: border-box; }
  html, body { width: 1200px; height: 784px; overflow: hidden; }
  body { background: var(--bg); font-family: "Open Sans", Arial, sans-serif; position: relative; }

  .card {
    position: absolute; width: 560px; height: 320px;
    border-radius: 3px; overflow: hidden;
    box-shadow: 0 6px 18px rgba(0,0,0,.18);
  }

  /* Front */
  .card-front {
    left: 50px; top: 70px;
    background: radial-gradient(ellipse at 40% 40%, #172653 0%, var(--navy) 55%, var(--navy-deep) 100%);
  }
  .card-front .brand { position: absolute; left: 40px; top: 108px; display: flex; align-items: center; gap: 16px; }
  .card-front .brand-mark { width: 96px; height: 96px; border-radius: 50%; border: 3px solid var(--white); flex: none; }
  .card-front .brand-name { color: var(--white); font-size: 34px; font-weight: 700; font-variant: small-caps; letter-spacing: 1px; line-height: 1; white-space: nowrap; }
  .card-front .brand-web { color: var(--blue); font-size: 11px; margin-top: 6px; text-align: right; }

  /* Back */
  .card-back { left: 590px; top: 394px; background: var(--white); }
  .card-back .brand { position: absolute; left: 30px; top: 36px; display: flex; align-items: center; gap: 14px; }
  .card-back .brand-mark { width: 80px; height: 80px; border-radius: 50%; border: 3px solid var(--navy); flex: none; }
  .card-back .brand-name { color: var(--navy); font-size: 30px; font-weight: 700; font-variant: small-caps; letter-spacing: 1px; line-height: 1; white-space: nowrap; }
  .card-back .brand-web { color: var(--blue); font-size: 10px; margin-top: 4px; text-align: right; }
  .card-back .faint-mark {
    position: absolute; right: -40px; top: 40px; width: 200px; height: 200px;
    border-radius: 50%; border: 6px solid var(--faint);
  }
  .person { position: absolute; left: 54px; top: 136px; z-index: 2; }
  .person-name { color: var(--blue); font-size: 18px; font-weight: 700; letter-spacing: .3px; line-height: 1.1; }
  .person-role { color: var(--muted); font-size: 11px; margin-bottom: 8px; }
  .contact-list { list-style: none; }
  .contact-list li { display: flex; align-items: center; gap: 8px; color: var(--ink); font-size: 13px; font-weight: 600; line-height: 19px; white-space: nowrap; }
  .contact-list svg { width: 12px; height: 12px; fill: var(--navy); flex: none; }

  .band { position: absolute; left: 0; right: 0; bottom: 0; width: 560px; height: 60px; display: block; }
</style>
</head>
<body>

<section class="card card-front">
  <div class="brand">
    <div class="brand-mark"></div>
    <div>
      <div class="brand-name">Pellworth Legal</div>
      <div class="brand-web">www.pellworthlegal.com.au</div>
    </div>
  </div>
</section>

<section class="card card-back">
  <div class="faint-mark"></div>
  <div class="brand">
    <div class="brand-mark"></div>
    <div>
      <div class="brand-name">Pellworth Legal</div>
      <div class="brand-web">www.pellworthlegal.com.au</div>
    </div>
  </div>

  <svg class="band" viewBox="0 0 560 60" preserveAspectRatio="none">
    <polygon points="560,0 560,60 0,60 0,50" fill="#3b7fd1"/>
    <polygon points="560,5 560,60 0,60 0,54" fill="#0d1a3a"/>
    <rect x="0" y="58" width="560" height="2" fill="#3b7fd1"/>
  </svg>

  <div class="person">
    <div class="person-name">DANA WHITFIELD</div>
    <div class="person-role">Manager</div>
    <ul class="contact-list">
      <li><svg viewBox="0 0 24 24"><path d="M6.6 10.8a15.1 15.1 0 0 0 6.6 6.6l2.2-2.2c.3-.3.7-.4 1-.2 1.1.4 2.3.6 3.6.6.6 0 1 .4 1 1V20c0 .6-.4 1-1 1A17 17 0 0 1 3 4c0-.6.4-1 1-1h3.5c.6 0 1 .4 1 1 0 1.3.2 2.5.6 3.6.1.3 0 .7-.2 1z"/></svg>0400 123 456</li>
      <li><svg viewBox="0 0 24 24"><path d="M7 1h10a2 2 0 0 1 2 2v18a2 2 0 0 1-2 2H7a2 2 0 0 1-2-2V3a2 2 0 0 1 2-2zm0 3v14h10V4z"/></svg>0400 987 654</li>
      <li><svg viewBox="0 0 24 24"><path d="M2 5h20v14H2zm2 2v.5l8 5 8-5V7l-8 5z"/></svg>info@pellworthlegal.com</li>
      <li><svg viewBox="0 0 24 24"><path d="M12 3l10 9h-3v9h-5v-6h-4v6H5v-9H2z"/></svg>po box, harbour street, Queensland</li>
    </ul>
  </div>
</section>

</body>
</html>
```